New company website for Redfern Hollow Building Company

We're looking to build a new company website that customers can use to contact us, get quotes, view past projects (renovations, additions, new construction, etc.), & learn more about our business. We want to use WordPress for our website and have already purchased the Divi theme (by Quillmark Studio). Using that theme isn't required but we already have several examples of websites that we want to model our site after that use this theme. The "look" we're after is simple, light, & clean.

Target Market(s)

Residential remodeling, renovations, and new construction.

Industry/Entity Type

Residential Construction

Coding

Coded - Design and coding required

Number of Pages Required

5+ page

Font styles to use
Sans Serif

Colors
33a6d7
aaaaaa

Requirements
Must have
• We require the website to be coded using the Divi theme. We'll be upgrading the project to include this today or tomorrow.
• The navigation bar should be static & remain at the top of the page. When scrolling we'd like the logo & info in the nav bar to size down. Here's an example of a site that does this: https://tovamerihomes.example/
Nice to have
• In the gallery with pictures of our finished product/jobs, when you mouse over the image, we'd like there to be additional info that shows up. For example, look at this gallery: https://tovamerihomes.example/projectcategories/kitchens/ We'll add a name/location of the job like: "Garvey kitchen - Apex, N.C."
• If you go to this website: https://plinvorworks.example/ and scroll down to the pictures, we like how the picture moves and is interactive.

```html
<!DOCTYPE html>
<html lang="en">
<head>
<meta charset="utf-8">
<title>Redfern Hollow Building Company</title>
<link rel="stylesheet" href="https://fonts.googleapis.com/css2?family=Saira+Semi+Condensed:wght@400;500;600&display=swap">
<style>
:root{
  --blue:#33a6d7;
  --ink:#3a3f47;
  --muted:#8b8f95;
  --grey:#aaaaaa;
  --page:#f3f3f3;
  --white:#ffffff;
  --footer:#474d56;
  --footer-bar:#5d636d;
  --field:#e9eaec;
}
*{box-sizing:border-box;margin:0;padding:0}
html,body{width:1200px;height:3719px;overflow:hidden}
body{background:var(--page);font-family:"Saira Semi Condensed",sans-serif;color:var(--ink);position:relative}
.abs{position:absolute}
.photo{position:absolute}
.label{position:absolute;font-size:13px;color:var(--muted);display:flex;align-items:center;gap:12px}
.label::after{content:"";width:44px;height:1px;background:var(--blue)}
.title{position:absolute;font-weight:500;font-size:25px;line-height:31px;color:var(--ink)}
.title em{font-style:normal;color:var(--blue)}
.copy{position:absolute;font-size:12.5px;line-height:19px;color:var(--muted)}
.btn{position:absolute;display:flex;align-items:center;justify-content:center;font-size:12px;background:var(--blue);color:var(--white)}
.btn-outline{background:transparent;border:1px solid var(--blue);color:var(--blue)}

/* header + hero */
.hero-card{left:53px;top:50px;width:1090px;height:610px;background:var(--white)}
.logo{left:77px;top:73px;width:240px;font-weight:600;font-size:18px;line-height:19px;color:var(--ink);letter-spacing:.5px}
.nav{left:360px;top:72px;width:783px;height:46px;border-bottom:1px solid #e3e3e3;display:flex;align-items:center;font-size:12.5px;color:var(--ink)}
.nav a{color:inherit;text-decoration:none;margin-right:40px}
.nav .current{color:var(--blue);border-top:2px solid var(--blue);padding-top:6px}
.nav .call{display:flex;align-items:center;gap:6px;margin-right:0}
.nav .call b{font-weight:600;color:var(--blue)}
.start{left:997px;top:78px;width:126px;height:32px}
.hero-photo{left:460px;top:133px;width:690px;height:477px;background:linear-gradient(180deg,#e7e4de 0%,#cfcac2 35%,#8a8178 60%,#5a524b 80%,#c9c3ba 100%)}
.thumb{top:505px;width:96px;height:100px;border:3px solid var(--white)}
.hero-label{left:153px;top:258px}
.hero-title{left:153px;top:283px;font-size:33px;line-height:41px;font-weight:500}
.hero-btn{left:153px;top:437px;width:130px;height:33px}
.arrow{position:absolute;width:30px;height:30px;border-radius:50%;display:flex;align-items:center;justify-content:center}

/* intro */
.intro-a{left:227px;top:726px;width:210px;height:245px;background:linear-gradient(160deg,#7e6e5e,#d8d1c7 55%,#9d8f80)}
.intro-b{left:330px;top:826px;width:203px;height:217px;border:6px solid var(--page);background:linear-gradient(180deg,#f1eee8,#bfae98 70%,#8a7763)}

/* specialties */
.spec{position:absolute}
.spec-tag{position:absolute;background:rgba(255,255,255,.86);padding:16px 18px}
.spec-tag h3{font-weight:500;font-size:15px;color:var(--ink);margin-bottom:8px}
.spec-tag p{font-size:11.5px;line-height:16px;color:var(--muted)}

/* portfolio */
.tabs{left:453px;top:1925px;width:510px;display:flex;gap:0;font-size:11.5px;color:var(--muted)}
.tabs span{flex:1;border-bottom:1px solid #cfcfcf;padding-bottom:5px}
.tabs .on{color:var(--blue);border-bottom-color:var(--blue)}
.gallery{left:77px;top:1977px;width:1050px;height:366px;display:flex}
.tile{position:relative;flex:1;overflow:hidden}
.tile .cap{position:absolute;left:22px;bottom:18px;color:var(--white);font-size:14px}
.tile .shade{position:absolute;left:0;right:0;bottom:0;height:90px;background:linear-gradient(180deg,rgba(0,0,0,0),rgba(0,0,0,.55))}
.tile .reveal{position:absolute;left:22px;top:205px;width:210px;color:var(--white)}
.reveal h4{font-weight:500;font-size:15px;margin-bottom:8px}
.reveal p{font-size:11.5px;line-height:16px;opacity:.95}
.reveal a{display:inline-block;margin-top:14px;font-size:11.5px;color:var(--white);border-bottom:1px solid var(--white)}

/* team */
.member{position:absolute;width:207px;height:190px}
.member .name{position:absolute;left:60px;top:40px;color:var(--white);font-size:13px}

/* footer */
.footer{left:53px;top:2943px;width:1100px;height:584px;background:var(--footer)}
.footer-bar{left:53px;top:3527px;width:1100px;height:56px;background:var(--footer-bar);color:#c9ccd0;font-size:11px;display:flex;align-items:center;padding-left:174px}
.footer-bar em{font-style:normal;color:var(--blue)}
.f-label{left:227px;top:3005px;color:#e6e7e9;font-size:12.5px}
.f-title{left:227px;top:3025px;font-weight:500;font-size:24px;color:var(--white)}
.f-title em{font-style:normal;color:var(--blue)}
.f-text{left:227px;font-size:12px;color:#d7d9dc}
.field{position:absolute;height:26px;background:var(--field);font-size:11px;color:#888;padding:5px 10px}
.map{left:667px;top:3010px;width:303px;height:373px;background:linear-gradient(135deg,#f0efe9,#e4e2da 50%,#ecebe4)}
.social{left:667px;top:3440px;display:flex;align-items:center;gap:7px;color:#e6e7e9;font-size:12px}
.social i{display:block;width:22px;height:22px;border-radius:50%;background:#e6e7e9}
.social i.on{background:var(--blue)}
</style>
</head>
<body>

<!-- header & hero -->
<div class="abs hero-card"></div>
<div class="abs logo">REDFERN HOLLOW<br>BUILDING COMPANY</div>
<nav class="abs nav">
  <a class="current">Home</a><a>Who We Are</a><a>Specialties</a><a>Portfolio</a><a>Contact Us</a>
  <span class="call">Call Us
    <svg width="16" height="16" viewBox="0 0 16 16"><circle cx="8" cy="8" r="7" fill="none" stroke="#33a6d7"/><path d="M5.5 4.5l1.6 1.4-.8 1.2c.5 1 1.3 1.8 2.3 2.3l1.2-.8 1.4 1.6-1 1c-2.8-.4-5.3-2.9-5.7-5.7z" fill="#33a6d7"/></svg>
    <b>919.555.0142</b></span>
</nav>
<div class="btn start">Getting Started</div>

<div class="photo hero-photo" role="img" aria-label="Bright white kitchen with island, bar stools and dark lower cabinets"></div>
<div class="photo thumb" style="left:854px;background:linear-gradient(160deg,#d9d4cc,#7d7268)" role="img" aria-label="Kitchen thumbnail"></div>
<div class="photo thumb" style="left:951px;background:linear-gradient(160deg,#bfb8ae,#5f5650)" role="img" aria-label="Kitchen thumbnail"></div>
<div class="photo thumb" style="left:1048px;width:99px;background:linear-gradient(160deg,#e8e5df,#a59a8d)" role="img" aria-label="Kitchen thumbnail"></div>

<div class="label hero-label">Redfern Hollow</div>
<h1 class="title hero-title">Add a Refreshing<br><em>New Look</em> to <em>Your</em><br><em>Home</em></h1>
<div class="btn btn-outline hero-btn">Contact Us</div>
<div class="arrow" style="left:155px;top:575px;border:1px solid #bbb">
  <svg width="10" height="10" viewBox="0 0 10 10"><path d="M6.5 1.5L3 5l3.5 3.5" fill="none" stroke="#777" stroke-width="1.4"/></svg></div>
<div class="arrow" style="left:192px;top:575px;background:#6c7077">
  <svg width="10" height="10" viewBox="0 0 10 10"><path d="M3.5 1.5L7 5 3.5 8.5" fill="none" stroke="#fff" stroke-width="1.4"/></svg></div>

<!-- intro -->
<div class="photo intro-a" role="img" aria-label="Living room with stone fireplace and wood beams"></div>
<div class="photo intro-b" role="img" aria-label="Open plan dining area with warm wood tones"></div>
<div class="label" style="left:610px;top:722px">Welcome to Redfern Hollow</div>
<h2 class="title" style="left:610px;top:745px;width:260px">We Specialize in <em>Remodeling</em>, New Home Construction and <em>Additions!</em></h2>
<p class="copy" style="left:610px;top:897px;width:300px">Contrary to popular belief, Lorem Ipsum is not simply random text. It has roots in a piece of classical Latin literature from 45 BC, making it over 2000 years old. Edmund Harlow, a Latin professor at Ashgrove College.</p>
<div class="btn" style="left:610px;top:1017px;width:130px;height:33px">Discover More</div>

<!-- specialties -->
<div class="label" style="left:153px;top:1115px">What We Do</div>
<h2 class="title" style="left:153px;top:1138px">Our <em>Specialties</em></h2>

<div class="photo spec" style="left:153px;top:1227px;width:380px;height:500px;background:linear-gradient(170deg,#f2efe9,#d9d1c4 45%,#8c7a64 75%,#c8c0b5)" role="img" aria-label="Remodeled kitchen with white cabinets and wood island"></div>
<div class="spec-tag" style="left:153px;top:1560px;width:267px;height:167px">
  <h3>Remodeling</h3><p>Contrary to popular belief, Lorem Ipsum is not simply random text. It has roots in a piece of classical.</p></div>

<div class="photo spec" style="left:613px;top:1117px;width:434px;height:320px;background:linear-gradient(170deg,#f3f1ec,#cfc4b4 55%,#7b6a58)" role="img" aria-label="New home living room with coffered ceiling and built-in shelves"></div>
<div class="spec-tag" style="left:700px;top:1287px;width:280px;height:150px">
  <h3 style="color:var(--blue)">New Home Construction</h3><p>Contrary to popular belief, Lorem Ipsum is not simply random text. It has roots in a piece of classical.</p></div>

<div class="photo spec" style="left:613px;top:1510px;width:434px;height:323px;background:linear-gradient(170deg,#e9ece9,#c2c7c2 45%,#a7876a 85%)" role="img" aria-label="Sunlit room addition with large windows and wood floor"></div>
<div class="spec-tag" style="left:627px;top:1677px;width:333px;height:150px">
  <h3>Additions</h3><p>Contrary to popular belief, Lorem Ipsum is not simply random text. It has roots in a piece of classical Latin literature.</p></div>

<!-- portfolio -->
<div class="label" style="left:153px;top:1895px">Portfolio</div>
<h2 class="title" style="left:153px;top:1918px">Our Recent <em>Work</em></h2>
<div class="abs tabs"><span>Before &amp; after</span><span class="on">Kitchens</span><span>Bathrooms</span><span>Whole house</span></div>
<div class="arrow" style="left:980px;top:1917px;border:1px solid #bbb">
  <svg width="10" height="10" viewBox="0 0 10 10"><path d="M6.5 1.5L3 5l3.5 3.5" fill="none" stroke="#777" stroke-width="1.4"/></svg></div>
<div class="arrow" style="left:1017px;top:1917px;background:#6c7077">
  <svg width="10" height="10" viewBox="0 0 10 10"><path d="M3.5 1.5L7 5 3.5 8.5" fill="none" stroke="#fff" stroke-width="1.4"/></svg></div>

<div class="abs gallery">
  <div class="tile" role="img" aria-label="White kitchen with black backsplash" style="background:linear-gradient(170deg,#efefef,#bdbdbd 45%,#3b3b3b 75%,#8e8e8e)"><div class="shade"></div><span class="cap">Lorem Ipsum</span></div>
  <div class="tile" role="img" aria-label="Kitchen with dark wood cabinets and range hood" style="background:linear-gradient(170deg,#8a6a4c,#3d2f25 50%,#6b5646)"><div class="shade"></div><span class="cap">Lorem Ipsum</span></div>
  <div class="tile" role="img" aria-label="Modern kitchen with stainless range hood" style="background:linear-gradient(170deg,#dedbd6,#a39c93 55%,#6c645c)">
    <svg class="abs" style="left:0;top:0" width="262" height="366" viewBox="0 0 262 366"><polygon points="0,190 262,110 262,366 0,366" fill="#33a6d7" fill-opacity=".92"/></svg>
    <div class="reveal"><h4>Lorem Ipsum</h4><p>Contrary to popular belief, Lorem Ipsum is not simply text random text.</p><a>View Detail</a></div>
  </div>
  <div class="tile" role="img" aria-label="Bright white kitchen with wood floor" style="background:linear-gradient(170deg,#f4f4f2,#d2cdc6 55%,#8d6e52)"><div class="shade"></div><span class="cap">Lorem Ipsum</span></div>
</div>
<div class="btn btn-outline" style="left:533px;top:2383px;width:134px;height:34px">View All Work</div>

<!-- team -->
<div class="label" style="left:227px;top:2572px">Team Member</div>
<h2 class="title" style="left:227px;top:2595px">Meet Our <em>Experts</em></h2>
<p class="copy" style="left:227px;top:2640px;width:250px">Contrary to popular belief, Lorem Ipsum is not simply random text. It has roots in a piece of classical Latin literature from 45 BC, making it over 2000 years old.</p>
<div class="btn" style="left:227px;top:2760px;width:116px;height:32px">More Info</div>

<div class="member" style="left:533px;top:2477px;background:linear-gradient(160deg,#4d7a3f,#2f4f2a 50%,#233448)" role="img" aria-label="Team member portrait"></div>
<div class="member" style="left:767px;top:2477px;background:linear-gradient(160deg,#3e6a34,#1f3a22 50%,#1f2d40)" role="img" aria-label="Team member portrait"><span class="name">Declan Whitfield</span></div>
<div class="member" style="left:533px;top:2687px;background:linear-gradient(160deg,#5e8a48,#36532f 50%,#223246)" role="img" aria-label="Team member portrait"></div>
<div class="member" style="left:767px;top:2687px;background:linear-gradient(160deg,#4a7a3a,#2b4828 50%,#20304a)" role="img" aria-label="Team member portrait"></div>

<!-- footer -->
<div class="abs footer"></div>
<div class="abs f-label">Redfern Hollow</div>
<h2 class="abs f-title">Contact <em>Us</em></h2>
<p class="abs f-text" style="top:3095px;line-height:18px">480 Larkspur Lane, Suite 2, Millbrook,<br>NC 27000</p>
<p class="abs f-text" style="top:3157px;display:flex;align-items:center;gap:6px;color:var(--blue)">Call Us
  <svg width="15" height="15" viewBox="0 0 16 16"><circle cx="8" cy="8" r="7" fill="none" stroke="#33a6d7"/><path d="M5.5 4.5l1.6 1.4-.8 1.2c.5 1 1.3 1.8 2.3 2.3l1.2-.8 1.4 1.6-1 1c-2.8-.4-5.3-2.9-5.7-5.7z" fill="#33a6d7"/></svg>
  <span style="color:var(--white)">919.555.0142</span></p>
<p class="abs f-text" style="top:3182px;color:var(--blue);text-decoration:underline">info@redfernhollow.example</p>

<div class="field" style="left:227px;top:3250px;width:185px">Name</div>
<div class="field" style="left:424px;top:3250px;width:186px">Phone</div>
<div class="field" style="left:227px;top:3286px;width:185px">Email</div>
<div class="field" style="left:424px;top:3286px;width:186px;display:flex;justify-content:space-between">Services<span>&#9662;</span></div>
<div class="field" style="left:227px;top:3322px;width:383px;height:68px">Message</div>
<div class="btn" style="left:227px;top:3425px;width:95px;height:32px">Send</div>

<div class="photo map" role="img" aria-label="Street map showing the office location"></div>
<svg class="abs" style="left:806px;top:3170px" width="24" height="32" viewBox="0 0 24 32"><path d="M12 1C6 1 1.5 5.5 1.5 11.5 1.5 19 12 31 12 31s10.5-12 10.5-19.5C22.5 5.5 18 1 12 1z" fill="#e0413a"/><circle cx="12" cy="11.5" r="4" fill="#fff"/></svg>
<div class="abs social">Get Social <i></i><i class="on"></i><i></i><i></i><i></i></div>

<div class="abs footer-bar">© 2018&nbsp;<em>Redfern Hollow</em>. All Rights Reserved</div>
<div class="abs" style="left:1030px;top:3547px;width:16px;height:16px;border-radius:50%;background:var(--blue)"></div>

</body>
</html>
```